I am looking for a Business Card Design for my spirit company titled "Harbor Cask" The company specializes in prohibition style/speakeasy mixology drinks and alcohol distribution. I am looking for Retro, Masculine, Sophisticated Card that embodies the look of Prohibition. Black and White colors. Also add Chatterly, Pictoro logo

Information that should go on the card is my Name, Title, Phone, Email, Website as follows:

Tobias R Grendle
Principal
415.867.2290
tobias@harborcask.com
harborcask.com
Updates

Hello all I have uploaded a pdf version of the logo. It seems as if some are saying the resolution is too small.

Target Market(s)

Male and Female drinkers of all ages with a sophisticated palate that have an appreciation for fine crafted cocktail

Industry/Entity Type

Business

Requirements
Must have
• Information that should go on the card is my Name, Title, Phone, Email, Website as follows:

Tobias R Grendle
Principal
415.867.2290
tobias@harborcask.com
harborcask.com

```html
<!DOCTYPE html>
<html lang="en">
<head>
<meta charset="utf-8">
<title>Harbor Cask — Business Card</title>
<link href="https://fonts.googleapis.com/css2?family=Roboto:wght@300;400&display=swap" rel="stylesheet">
<style>
  :root {
    --stage: #3b3b3b;
    --card-white: #ffffff;
    --card-dark: #3d3d3d;
    --ink: #2a2a2a;
    --ink-soft: #6f6f6f;
    --ring: #ececec;
    --rule: #d4d4d4;
  }
  * { box-sizing: border-box; margin: 0; padding: 0; }
  html, body {
    width: 1200px; height: 900px; overflow: hidden;
    background: var(--stage);
    font-family: "Roboto", Arial, sans-serif;
  }
  .card {
    position: absolute;
    left: 320px;
    width: 560px; height: 320px;
    box-shadow: 0 6px 18px rgba(0,0,0,.35);
    overflow: hidden;
  }
  /* back of card */
  .card-back { top: 80px; background: var(--card-dark); }
  .card-back .center-panel {
    position: absolute; left: 170px; top: 0;
    width: 310px; height: 100%;
    background: var(--card-white);
  }
  /* front of card */
  .card-front { top: 490px; background: var(--card-white); }

  .brand {
    position: absolute;
    width: 260px; height: 220px;
    display: flex; align-items: center; justify-content: center;
  }
  .brand-ring {
    position: absolute; left: 30px; top: 10px;
    width: 200px; height: 200px;
    border: 10px solid var(--ring); border-radius: 50%;
  }
  .brand-name {
    position: relative;
    font-weight: 400; font-size: 40px; line-height: 1.05;
    color: var(--ink); text-align: center;
  }
  .card-back .brand { left: 195px; top: 50px; }
  .card-front .brand { left: 20px; top: 50px; }

  .divider {
    position: absolute; left: 290px; top: 40px;
    width: 1px; height: 200px;
    background: linear-gradient(var(--card-white), var(--rule) 30%, var(--rule) 70%, var(--card-white));
  }
  .contact { position: absolute; left: 312px; top: 62px; color: var(--ink); }
  .contact-name { font-weight: 300; font-size: 23px; letter-spacing: .2px; }
  .contact-title { font-weight: 300; font-size: 12px; color: var(--ink-soft); margin-top: 4px; }
  .contact-list { list-style: none; margin-top: 28px; }
  .contact-list li {
    display: flex; align-items: center; gap: 9px;
    font-weight: 300; font-size: 13px; color: var(--ink-soft);
    margin-bottom: 4px;
  }
  .contact-list svg { width: 12px; height: 12px; flex: none; }
</style>
</head>
<body>
  <section class="card card-back" aria-label="Card back">
    <div class="center-panel"></div>
    <div class="brand">
      <div class="brand-ring"></div>
      <p class="brand-name">Harbor<br>Cask</p>
    </div>
  </section>

  <section class="card card-front" aria-label="Card front">
    <div class="brand">
      <div class="brand-ring"></div>
      <p class="brand-name">Harbor<br>Cask</p>
    </div>
    <div class="divider"></div>
    <div class="contact">
      <h1 class="contact-name">Tobias R Grendle</h1>
      <p class="contact-title">Principal</p>
      <ul class="contact-list">
        <li>
          <svg viewBox="0 0 12 12" aria-hidden="true"><path d="M1 4 Q6 0 11 4 L9.5 5.5 L8 4.5 L4 4.5 L2.5 5.5 Z M2.5 6 H9.5 L10.5 11 H1.5 Z" fill="#2a2a2a"/></svg>
          <span>415.867.2290</span>
        </li>
        <li>
          <svg viewBox="0 0 12 12" aria-hidden="true"><rect x="0.5" y="2" width="11" height="8" fill="#2a2a2a"/><path d="M0.5 2 L6 6.5 L11.5 2" stroke="#fff" stroke-width="1" fill="none"/></svg>
          <span>tobias@harborcask.com</span>
        </li>
        <li>
          <svg viewBox="0 0 12 12" aria-hidden="true"><circle cx="6" cy="6" r="5.5" fill="#2a2a2a"/><path d="M0.5 6 H11.5 M6 0.5 V11.5 M2 3.5 H10 M2 8.5 H10" stroke="#fff" stroke-width=".7"/><ellipse cx="6" cy="6" rx="2.4" ry="5.5" stroke="#fff" stroke-width=".7" fill="none"/></svg>
          <span>harborcask.com</span>
        </li>
      </ul>
    </div>
  </section>
</body>
</html>
```